K.E.L Ventures - Business Card

We need a business card design for a new company based in Malaysia, called K.E.L Ventures Sdn. Bhd. We create, develop & customize database & software/web-based business systems to suit our clients need, mainly in oil&gas industry.

We would like to challenge the creativity of you to design a simple, meaningful, modern, professional & sleek. The design concept may varies but worthy enough for the recipients to proudly keep it in their wallet, and award us with fruitful business opportunities.

B-3-12 Meridan Plaza,
SS21/4, Subang Jaya,
46300 Selangor. Malaysia

http://kelventures-example.com

HAFIZ Roslan | +6012-3817260 | Co-Founder
Di Nazwan | +6012-4092731 | Co-Founder
Abdul Kamil | +6019-5063184 | Managing Director

Target Market(s)

The target market will expand to several other industries such as aviation, communication, automotive, education & hotel.

Industry/Entity Type

Business

Font styles to use
Serif
Sans Serif
Decorative
Script

Requirements
Must have
• plain background yet colourful concept.
Should not have
• something too easy that I can draw myself

```html
<!DOCTYPE html>
<html lang="en">
<head>
<meta charset="utf-8">
<title>K.E.L Ventures – Business Card</title>
<link rel="stylesheet" href="https://fonts.googleapis.com/css2?family=Lato:wght@400;700&display=swap">
<style>
  :root {
    --stage: #8c8c8c;
    --card: #050505;
    --green: #8cc63f;
    --white: #ffffff;
    --coral: #e2505f;
    --teal: #1d8c90;
    --field-green: #1c8a48;
    --field-blue: #27359a;
    --field-violet: #3a2470;
  }
  * { box-sizing: border-box; margin: 0; padding: 0; }
  html, body {
    width: 1200px;
    height: 900px;
    overflow: hidden;
    background: var(--stage);
    font-family: "Lato", Arial, sans-serif;
  }
  .card {
    position: absolute;
    left: 120px;
    top: 176px;
    width: 960px;
    height: 548px;
    border-radius: 22px;
    background: var(--card);
    overflow: hidden;
  }
  .pattern-field {
    position: absolute;
    left: 0;
    top: 0;
    width: 620px;
    height: 100%;
    background: linear-gradient(to right,
      var(--field-green) 0%,
      var(--field-blue) 38%,
      var(--field-violet) 62%,
      var(--card) 100%);
  }
  .details {
    position: absolute;
    right: 62px;
    top: 140px;
    display: flex;
    flex-direction: column;
    align-items: flex-end;
  }
  .name {
    font-size: 48px;
    line-height: 1.1;
    color: var(--green);
    font-weight: 400;
  }
  .name strong { font-weight: 700; }
  .role {
    font-size: 22px;
    color: var(--white);
    font-weight: 400;
    margin-top: 0;
  }
  .contact {
    margin-top: 26px;
    display: flex;
    flex-direction: column;
    align-items: flex-end;
    gap: 6px;
  }
  .tag {
    display: inline-block;
    color: var(--white);
    white-space: nowrap;
  }
  .tag--coral {
    background: var(--coral);
    font-size: 29px;
    line-height: 38px;
    padding: 0 10px;
  }
  .tag--teal {
    background: var(--teal);
    font-size: 21px;
    line-height: 29px;
    padding: 0 9px;
  }
  .address {
    margin-top: 24px;
    display: flex;
    flex-direction: column;
    align-items: flex-end;
    gap: 3px;
    font-style: normal;
  }
</style>
</head>
<body>
  <div class="card">
    <div class="pattern-field" role="img" aria-label="Decorative pixel mosaic in green, teal, blue and violet fading into black"></div>
    <div class="details">
      <h1 class="name">Di <strong>Nazwan</strong></h1>
      <p class="role">Co-Founder</p>
      <div class="contact">
        <span class="tag tag--coral">+6012-4092731</span>
        <span class="tag tag--coral">http://kelventures-example.com</span>
      </div>
      <address class="address">
        <span class="tag tag--teal">B-3-12 Meridan Plaza</span>
        <span class="tag tag--teal">SS21/4, Subang Jaya</span>
        <span class="tag tag--teal">46300 Selangor. Malaysia</span>
      </address>
    </div>
  </div>
</body>
</html>
```